WordPress Site That Reviews Footwear

We need a wordpress web design for an affiliate site called TreadNest. We review and do roundups on footwear products. The final design should be clean and mobile friendly. The site should be built with Gutenberg page builder. We like the design of https://dermalquill.com/.
Updates

Need extra days to review

Target Market(s)

USA

Industry/Entity Type

Footwear

Logo Text

TreadNest

Number of Pages Required

4 page

Font styles to use
Serif
Sans Serif

Requirements
Must have
• Wordpress site
Blog post
Page
Categories
Homepage

```html
<!DOCTYPE html>
<html lang="en">
<head>
<meta charset="utf-8">
<title>TreadNest – Expert Footwear Advice</title>
<link href="https://fonts.googleapis.com/css2?family=Jost:wght@400;500;600;700&family=Poppins:wght@400;500;600&display=swap" rel="stylesheet">
<style>
:root{
  --blue:#1f4fb3;
  --blue-bright:#2456c4;
  --navy:#0a2a6e;
  --navy-deep:#041848;
  --ink:#0b0f1c;
  --night:#050a1a;
  --text:#1b1b1b;
  --muted:#666;
  --line:#b9bfcc;
  --white:#fff;
  --grey-soft:#e9ebef;
}
*{box-sizing:border-box;margin:0;padding:0}
html,body{width:1200px;height:2884px;overflow:hidden;background:var(--white)}
body{position:relative;font-family:'Jost',sans-serif;color:var(--text)}
.abs{position:absolute}
a{color:inherit;text-decoration:none}

/* header */
.site-header{position:absolute;left:0;top:0;width:1200px;height:88px;background:var(--white)}
.brand{position:absolute;left:88px;top:22px;display:flex;align-items:center;gap:10px;font-family:'Jost',sans-serif;font-weight:700;font-size:33px;color:var(--blue);letter-spacing:.3px}
.brand-dot{width:32px;height:32px;border-radius:50%;background:var(--blue)}
.main-nav{position:absolute;left:486px;top:37px;display:flex;gap:37px;font-family:'Poppins',sans-serif;font-size:12.5px;letter-spacing:1px;color:#222}
.main-nav .active{color:var(--blue);border-bottom:2px solid var(--blue);padding-bottom:3px}
.social{position:absolute;display:flex;gap:12px}
.social span{width:16px;height:16px;border-radius:50%;background:#111;display:block}
.header-social{left:1013px;top:37px}

/* hero */
.hero{position:absolute;left:0;top:88px;width:1200px;height:472px;background:radial-gradient(ellipse at 60% 40%,#1746a6 0%,#0c2f7e 45%,#071f5a 100%);overflow:hidden}
.hero-curve{position:absolute;left:0;top:528px;width:1200px;height:40px}
.hero h1{position:absolute;left:87px;top:170px;font-weight:500;font-size:36px;line-height:43px;color:var(--white)}
.btn{display:flex;align-items:center;justify-content:center;border-radius:22px;font-family:'Poppins',sans-serif;font-weight:500;color:var(--white);background:var(--blue-bright)}
.hero .btn{position:absolute;left:89px;top:283px;width:161px;height:40px;font-size:15px}
.type-card{position:absolute;width:160px;height:118px;background:var(--white);border-radius:3px;text-align:center;font-family:'Poppins',sans-serif;font-weight:500;font-size:15px;color:#111}
.type-card .icon{width:80px;height:50px;margin:22px auto 10px;border-radius:6px;background:linear-gradient(#e4e9f5,#cdd6ec)}

/* footwear type */
.section-title{position:absolute;left:0;width:1200px;text-align:center;font-weight:600;color:var(--blue);font-size:33px}
.section-sub{position:absolute;left:0;width:1200px;text-align:center;font-size:15.5px;line-height:20px;color:#222}
.cat-band{position:absolute;left:0;top:752px;width:768px;height:528px;background:linear-gradient(160deg,#0a2d78 0%,#061f5c 55%,#041848 100%)}
.cat-box{position:absolute;width:248px;height:183px;border:2px solid #1e4fb0;text-align:center;color:var(--white)}
.cat-box h3{margin-top:20px;font-weight:500;font-size:23px}
.cat-box p{margin:10px auto 0;width:200px;font-size:13.5px;line-height:17.5px;color:#b8c2dc}
.cat-box .pill{margin:13px auto 0;width:110px;height:28px;border:1.5px solid var(--white);border-radius:14px;font-family:'Poppins',sans-serif;font-size:10.5px;font-weight:500;display:flex;align-items:center;justify-content:center}
.cat-photo{position:absolute;left:738px;top:792px;width:409px;height:437px;background:radial-gradient(ellipse at 55% 55%,#5a1218 0%,#1c1d24 50%,#0b0c12 100%);box-shadow:0 10px 30px rgba(0,0,0,.25)}

/* reviews */
.quote-badge{position:absolute;left:570px;top:1415px;width:60px;height:60px;border-radius:50%;background:var(--grey-soft);display:flex;align-items:center;justify-content:center;color:var(--blue);font-family:'Jost',sans-serif;font-weight:700;font-size:48px;line-height:1;padding-top:18px}
.review-text{position:absolute;left:210px;top:1494px;width:780px;text-align:center;font-family:'Poppins',sans-serif;font-size:13.5px;line-height:20px;color:#222}
.review-meta{position:absolute;left:0;top:1582px;width:1200px;display:flex;justify-content:center;align-items:center;gap:14px;font-family:'Poppins',sans-serif}
.review-meta .date{display:flex;align-items:center;gap:8px;font-size:11px;color:#333}
.review-meta .sep{width:1px;height:14px;background:#ccc}
.review-meta .name{font-weight:500;font-size:13.5px}
.dots{position:absolute;left:576px;top:1629px;display:flex;gap:8px}
.dots span{width:10px;height:10px;border-radius:50%;border:1px solid #999}
.dots .on{background:var(--blue);border-color:var(--blue)}

/* blogs */
.blog-band{position:absolute;left:0;top:1700px;width:1200px;height:470px}
.blog-card{position:absolute;top:1865px;width:325px;height:192px;background:var(--white);font-family:'Jost',sans-serif}
.blog-date{position:absolute;left:20px;top:16px;width:50px;text-align:center;color:var(--blue);font-weight:600;font-size:33px;line-height:34px}
.blog-date small{display:block;font-size:11px;line-height:12px;color:#444;font-weight:500}
.blog-card h4{position:absolute;left:95px;top:22px;width:210px;font-weight:600;font-size:16px;line-height:18px;color:#111}
.blog-card p{position:absolute;left:95px;top:75px;width:210px;font-size:12px;line-height:17.5px;color:#555}
.blog-card .more{position:absolute;left:95px;top:141px;width:106px;height:27px;border:1px solid #999;border-radius:14px;font-size:10.5px;display:flex;align-items:center;justify-content:center;color:#222}

/* inquiry */
.field{position:absolute;height:34px;border-bottom:1px solid var(--line);display:flex;align-items:center;gap:10px;padding-left:8px;font-family:'Poppins',sans-serif;font-size:13px;color:#888}
.submit{position:absolute;left:533px;top:2442px;width:134px;height:40px;font-size:15px}

/* footer */
.site-footer{position:absolute;left:0;top:2561px;width:1200px;height:281px;background:#000;color:var(--white)}
.foot-brand{position:absolute;left:88px;top:110px;font-weight:700;font-size:33px;color:var(--blue)}
.foot-dot{position:absolute;left:150px;top:72px;width:30px;height:30px;border-radius:50%;background:var(--white)}
.foot-social{left:100px;top:180px;gap:22px}
.foot-social span{background:var(--white)}
.foot-head{position:absolute;top:63px;font-weight:500;font-size:18px;color:var(--blue-bright)}
.foot-links{position:absolute;left:328px;top:106px;list-style:none;font-size:13.5px;line-height:26.5px}
.foot-links .current{color:var(--blue-bright);text-decoration:underline}
.contact-row{position:absolute;left:513px;display:flex;gap:14px;font-size:13.5px;line-height:19px}
.contact-row svg{flex:none;margin-top:2px}
.map{position:absolute;left:800px;top:56px;width:312px;height:176px;border-radius:6px;background:linear-gradient(135deg,#eef0f3,#dfe3e8)}
.copyright{position:absolute;left:0;top:2842px;width:1200px;height:42px;background:var(--blue);color:var(--white);font-size:12.5px;display:flex;align-items:center;justify-content:center}
</style>
</head>
<body>

<header class="site-header">
  <a class="brand" href="#"><span class="brand-dot"></span>TreadNest</a>
  <nav class="main-nav">
    <a class="active" href="#">HOME</a><a href="#">ABOUT</a><a href="#">PRODUCTS</a><a href="#">REVIEWS</a><a href="#">CONTACT US</a>
  </nav>
  <div class="social header-social" aria-label="Social links"><span></span><span></span><span></span><span></span></div>
</header>

<section class="hero">
  <h1>Expert Footwear advice,<br>based on science</h1>
  <a class="btn" href="#">Explore More</a>
  <div class="type-card" style="left:576px;top:101px"><div class="icon" role="img" aria-label="Running shoe icon"></div>Running</div>
  <div class="type-card" style="left:760px;top:101px"><div class="icon" role="img" aria-label="Trail running shoe icon"></div>Trail running</div>
  <div class="type-card" style="left:944px;top:101px"><div class="icon" role="img" aria-label="Hiking boot icon"></div>Hiking boots</div>
  <div class="type-card" style="left:536px;top:243px"><div class="icon" role="img" aria-label="Hiking shoe icon"></div>Hiking shoes</div>
  <div class="type-card" style="left:720px;top:243px"><div class="icon" role="img" aria-label="Track spike icon"></div>Track and field</div>
  <div class="type-card" style="left:904px;top:243px"><div class="icon" role="img" aria-label="Walking shoe icon"></div>Walking</div>
</section>
<svg class="hero-curve" viewBox="0 0 1200 40" preserveAspectRatio="none" aria-hidden="true">
  <path d="M0 32 Q600 -12 1200 32 L1200 0 L0 0Z" fill="#071f5a"/>
  <path d="M0 32 Q600 -12 1200 32 L1200 40 Q600 0 0 40Z" fill="#000"/>
  <path d="M0 40 Q600 0 1200 40Z" fill="#fff"/>
</svg>

<h2 class="section-title" style="top:608px">What’s your Footwear type?</h2>
<p class="section-sub" style="top:662px">Lorem Ipsum is simply dummy text of the printing and<br>typesetting industry.</p>

<section class="cat-band">
  <div class="cat-box" style="left:136px;top:65px"><h3>Men Shoes</h3><p>Lorem Ipsum is simply dummy text of the printing and typesetting industry.</p><a class="pill" href="#">VIEW MORE</a></div>
  <div class="cat-box" style="left:409px;top:65px"><h3>Women Shoes</h3><p>Lorem Ipsum is simply dummy text of the printing and typesetting industry.</p><a class="pill" href="#">VIEW MORE</a></div>
  <div class="cat-box" style="left:136px;top:273px"><h3>kids Shoes</h3><p>Lorem Ipsum is simply dummy text of the printing and typesetting industry.</p><a class="pill" href="#">VIEW MORE</a></div>
  <div class="cat-box" style="left:409px;top:273px"><h3>Baby Shoes</h3><p>Lorem Ipsum is simply dummy text of the printing and typesetting industry.</p><a class="pill" href="#">VIEW MORE</a></div>
</section>
<div class="cat-photo" role="img" aria-label="Pair of white sneakers over a red brush stroke inside a grey frame on a dark background"></div>

<h2 class="section-title" style="top:1350px">Reviews</h2>
<div class="quote-badge" aria-hidden="true">“</div>
<p class="review-text">Lorem Ipsum is simply dummy text of the printing and typesetting industry. Lorem Ipsum has been the industry's standard dummy text ever since the 1500s, when an unknown printer took a galley of type and scrambled it to make a type specimen book.</p>
<div class="review-meta">
  <span class="date"><svg width="15" height="15" viewBox="0 0 16 16"><rect x="1.5" y="3" width="13" height="11.5" rx="1" fill="none" stroke="#1f4fb3" stroke-width="1.6"/><path d="M1.5 6.5h13M5 1v3M11 1v3" stroke="#1f4fb3" stroke-width="1.6"/></svg>30 Nov, 2020</span>
  <span class="sep"></span>
  <span class="name">Marla Jennings</span>
</div>
<div class="dots"><span></span><span class="on"></span><span></span></div>

<svg class="blog-band" viewBox="0 0 1200 470" preserveAspectRatio="none" aria-hidden="true">
  <defs><linearGradient id="night" x1="0" y1="0" x2="1" y2="1"><stop offset="0" stop-color="#03081a"/><stop offset="1" stop-color="#081a3e"/></linearGradient></defs>
  <path d="M0 14 Q600 24 1200 12 L1200 458 Q600 445 0 458Z" fill="url(#night)"/>
</svg>
<h2 class="section-title" style="top:1792px;color:#fff">Blogs</h2>
<article class="blog-card" style="left:88px"><div class="blog-date">18<small>Jun, 21</small></div><h4>Lorem Ipsum is simply dummy text of the printing</h4><p>Lorem Ipsum has been the industry's standard dummy text ever since the 1500s, when an unknown...</p><a class="more" href="#">READ MORE</a></article>
<article class="blog-card" style="left:437px"><div class="blog-date">10<small>Jun, 21</small></div><h4>Lorem Ipsum is simply dummy text of the printing</h4><p>Lorem Ipsum has been the industry's standard dummy text ever since the 1500s, when an unknown...</p><a class="more" href="#">READ MORE</a></article>
<article class="blog-card" style="left:787px"><div class="blog-date">07<small>Jun, 21</small></div><h4>Lorem Ipsum is simply dummy text of the printing</h4><p>Lorem Ipsum has been the industry's standard dummy text ever since the 1500s, when an unknown...</p><a class="more" href="#">READ MORE</a></article>

<h2 class="section-title" style="top:2223px">Quick Inquiry</h2>
<div class="field" style="left:201px;top:2296px;width:250px"><svg width="14" height="14" viewBox="0 0 14 14"><circle cx="7" cy="4.5" r="3" fill="none" stroke="#1f4fb3" stroke-width="1.4"/><path d="M1.5 13.5c0-3 2.5-5 5.5-5s5.5 2 5.5 5" fill="none" stroke="#1f4fb3" stroke-width="1.4"/></svg>Name</div>
<div class="field" style="left:475px;top:2296px;width:250px"><svg width="14" height="14" viewBox="0 0 14 14"><rect x="3" y="1" width="8" height="12" rx="1.5" fill="none" stroke="#1f4fb3" stroke-width="1.4"/><path d="M6 11h2" stroke="#1f4fb3" stroke-width="1.4"/></svg>Phone</div>
<div class="field" style="left:749px;top:2296px;width:250px"><svg width="15" height="14" viewBox="0 0 15 14"><rect x="1" y="2.5" width="13" height="9" rx="1" fill="none" stroke="#1f4fb3" stroke-width="1.4"/><path d="M1 3l6.5 5 6.5-5" fill="none" stroke="#1f4fb3" stroke-width="1.4"/></svg>Email</div>
<div class="field" style="left:201px;top:2368px;width:798px"><svg width="14" height="14" viewBox="0 0 14 14"><rect x="1" y="1.5" width="11" height="11" rx="1" fill="none" stroke="#1f4fb3" stroke-width="1.4"/><path d="M5 9l1-3 5-5 2 2-5 5z" fill="#fff" stroke="#1f4fb3" stroke-width="1.2"/></svg>Message</div>
<a class="btn submit" href="#">Submit</a>

<footer class="site-footer">
  <span class="foot-dot"></span>
  <div class="foot-brand">TreadNest</div>
  <div class="social foot-social" aria-label="Social links"><span></span><span></span><span></span><span></span></div>

  <h3 class="foot-head" style="left:328px">Quick Link</h3>
  <ul class="foot-links">
    <li class="current">Home</li><li>About Us</li><li>Products</li><li>Testimonials</li><li>Contact Us</li>
  </ul>

  <h3 class="foot-head" style="left:513px">Conatct info</h3>
  <div class="contact-row" style="top:106px"><svg width="16" height="18" viewBox="0 0 16 18"><path d="M8 17s6-6 6-10.5A6 6 0 0 0 2 6.5C2 11 8 17 8 17z" fill="none" stroke="#2456c4" stroke-width="1.8"/><circle cx="8" cy="6.5" r="2.2" fill="#2456c4"/></svg><span>128 Harbor Lane,<br>Fairview, OR&nbsp;&nbsp;&nbsp;97024</span></div>
  <div class="contact-row" style="top:163px"><svg width="16" height="16" viewBox="0 0 16 16"><path d="M3 1l3 3-1.5 2.5a9 9 0 0 0 5 5L12 10l3 3-2 2C7 15 1 9 1 3z" fill="#2456c4"/></svg><span>503.555.0148</span></div>
  <div class="contact-row" style="top:201px"><svg width="16" height="14" viewBox="0 0 16 14"><rect x="1" y="2" width="14" height="10" fill="none" stroke="#2456c4" stroke-width="1.6"/><path d="M1 2l7 6 7-6" fill="none" stroke="#2456c4" stroke-width="1.6"/></svg><span>info@treadnest.com</span></div>

  <div class="map" role="img" aria-label="Street map showing the store location"></div>
</footer>
<div class="copyright">Copyright © 2021 TreadNest. All Rights Reserved</div>

</body>
</html>
```